Emerging Australian photographer

I'm based in Cunderdin, a small rural town in the Wheatbelt area of Western Australia. So its a good thing that I love to travel further afield both for pleasure and for work. To me that is one and the same thing in any event!

My desire is to take photos that make the viewers heart skip. I love taking photos of people doing the things they love or being with the people they love. For me, the joy of photography comes with capturing the 'moments between the moments'. I like candid photography best of all - like when the new husband is staring joyfully at his bride and at that minute is unaware of the photographer capturing the moment.

I am available for weddings, engagements, birthdays, special events, newborns, family or individual portraits. By the end of the year I will be accredited with the Coastal Guild of Image Artisans.

I need a card that stands out but is elegant and would sit well on the table at a wedding or be given out in the church grounds. Classy and a little bit sassy.

Target Market(s)

Consumers who are seeking photographic services, eg wedding guests who see me at work and make enquiries.

Industry/Entity Type

Church

Contact Information for Business Card

Tamsin Bexley Photography
Tamsin Bexley
0452 307 618
www.tamsinbexley.com.au
photos@tamsinbexley.com.au

Requirements
Must have
• Must fit with the theme in the watermarks, but be crisp and modern.
Nice to have
• However it's not essential to have the pink! Facebook and Twitter logos.
Should not have
• Old style fonts like times new roman.

```html
<!DOCTYPE html>
<html lang="en">
<head>
<meta charset="UTF-8">
<title>Tamsin Bexley Photography – Business Card</title>
<link rel="stylesheet" href="https://fonts.googleapis.com/css2?family=Mulish:wght@300;400;700&display=swap">
<style>
  :root {
    --page-bg: #ffffff;
    --card-bg: #ffffff;
    --ink-grey: #5f5f61;
    --text-grey: #9a9a9c;
    --blush: #f7c6d9;
    --blush-strong: #f4a8c6;
    --card-shadow: rgba(0, 0, 0, 0.14);
  }
  * { box-sizing: border-box; margin: 0; padding: 0; }
  html, body {
    width: 1200px;
    height: 1200px;
    overflow: hidden;
    background: var(--page-bg);
    font-family: "Mulish", "Helvetica Neue", Arial, sans-serif;
  }
  .sheet {
    position: relative;
    width: 1200px;
    height: 1200px;
  }
  .card {
    position: absolute;
    width: 693px;
    height: 427px;
    background: var(--card-bg);
    box-shadow: 0 4px 14px var(--card-shadow);
    overflow: hidden;
  }
  .card--front { left: 250px; top: 142px; }
  .card--back  { left: 262px; top: 638px; }

  /* front */
  .brand {
    position: absolute;
    left: 0;
    right: 0;
    top: 222px;
    display: flex;
    align-items: center;
    justify-content: center;
    gap: 14px;
  }
  .brand__dot {
    width: 14px;
    height: 14px;
    border-radius: 50%;
    background: var(--blush-strong);
  }
  .brand__name {
    font-size: 38px;
    font-weight: 300;
    line-height: 1.2;
    color: var(--ink-grey);
    letter-spacing: 0.4px;
  }

  /* back */
  .base-band {
    position: absolute;
    left: 0;
    top: 0;
    width: 100%;
    height: 100%;
  }
  .holder-name {
    position: absolute;
    left: 94px;
    top: 102px;
    font-size: 23px;
    font-weight: 700;
    line-height: 1.2;
    color: var(--blush-strong);
    letter-spacing: 1.2px;
  }
  .contact-list {
    position: absolute;
    left: 98px;
    top: 193px;
    list-style: none;
    z-index: 2;
  }
  .contact-list li {
    display: flex;
    align-items: center;
    gap: 10px;
    height: 31px;
    font-size: 19px;
    font-weight: 300;
    color: var(--text-grey);
    letter-spacing: 0.6px;
    white-space: nowrap;
  }
  .contact-icon {
    width: 15px;
    height: 15px;
    flex: none;
  }
</style>
</head>
<body>
<main class="sheet">

  <section class="card card--front" aria-label="Card front">
    <div class="brand">
      <span class="brand__dot"></span>
      <span class="brand__name">Tamsin Bexley Photography</span>
    </div>
  </section>

  <section class="card card--back" aria-label="Card back">
    <svg class="base-band" viewBox="0 0 480 296" preserveAspectRatio="none" aria-hidden="true">
      <path fill="var(--blush)" d="M0,220 C60,200 150,215 250,240 C330,258 420,240 480,228 L480,296 L0,296 Z"/>
    </svg>

    <h1 class="holder-name">Tamsin Bexley</h1>

    <ul class="contact-list">
      <li>
        <svg class="contact-icon" viewBox="0 0 16 16" aria-hidden="true">
          <circle cx="8" cy="8" r="8" fill="var(--blush-strong)"/>
          <rect x="6" y="4" width="4" height="8" rx="1" fill="#fff"/>
        </svg>
        0452 307 618
      </li>
      <li>
        <svg class="contact-icon" viewBox="0 0 16 16" aria-hidden="true">
          <circle cx="8" cy="8" r="8" fill="var(--blush-strong)"/>
          <rect x="4" y="5" width="8" height="6" fill="#fff"/>
          <path d="M4,5 L8,8.5 L12,5" fill="none" stroke="var(--blush-strong)" stroke-width="1"/>
        </svg>
        photos@tamsinbexley.com.au
      </li>
      <li>
        <svg class="contact-icon" viewBox="0 0 16 16" aria-hidden="true">
          <circle cx="8" cy="8" r="8" fill="var(--blush-strong)"/>
          <circle cx="8" cy="8" r="4" fill="none" stroke="#fff" stroke-width="1.2"/>
          <line x1="4" y1="8" x2="12" y2="8" stroke="#fff" stroke-width="1"/>
        </svg>
        www.tamsinbexley.com.au
      </li>
    </ul>
  </section>

</main>
</body>
</html>
```